E-mail newsletter design - tolvexcraft

We are a gaming app developer

When an in-app game finishes, we would like to mail people taking part in leagues with a table showing where they finished along with all other players.

There could be up to 20 players in each league.

The mail shows the name of the league they are in and has an announcement regarding the game currently going on.

The mail should be HTML formatted and follow the look and feel of our website

Mail should be branded based on which app is sending the mail
tolvex startline - see tolvexstartline.example
tolvex scrumba - see tolvexscrumba.example
tolvex quizzle see tolvexquizzle.example

It should include a graphic element that is able to be written over, containing the placeholder text "Don't forget to play (name of next game) starting on (date)"

Requirements
Must have
• Any graphical elements should be provided separately

```html
<!DOCTYPE html>
<html lang="en">
<head>
<meta charset="utf-8">
<title>tolvex startline – League Table</title>
<link href="https://fonts.googleapis.com/css2?family=Jost:wght@300;400;600;700&display=swap" rel="stylesheet">
<style>
  :root {
    --header-bg: #f1f1f1;
    --page-top: #d6d6d6;
    --page-bottom: #ffffff;
    --panel-bg-a: #e8e8e9;
    --panel-bg-b: #d7e3ea;
    --headcell-bg: #5b5b5b;
    --headcell-text: #ffffff;
    --cell-bg: #ffffff;
    --text-dark: #3a3a3a;
    --text-strong: #111111;
    --accent-red: #c0161b;
    --brand-blue: #1e4f7c;
    --footer-bg: #f4f4f4;
  }
  * { box-sizing: border-box; margin: 0; padding: 0; }
  html, body { width: 1200px; height: 1008px; overflow: hidden; }
  body {
    font-family: "Jost", sans-serif;
    background: linear-gradient(to bottom, var(--page-top) 185px, var(--page-bottom) 640px);
    position: relative;
  }
  .mail-header {
    position: absolute; left: 0; top: 0; width: 1200px; height: 185px;
    background: var(--header-bg);
    border-bottom: 1px solid #555;
    box-shadow: 0 4px 10px rgba(0,0,0,0.35);
  }
  .sender {
    position: absolute; left: 502px; top: 86px;
    display: flex; align-items: baseline; gap: 12px;
  }
  .sender-from { font-weight: 300; font-size: 24px; color: #555; }
  .sender-brand { font-weight: 600; font-size: 28px; color: var(--brand-blue); }
  .league-panel {
    position: absolute; left: 265px; top: 197px; width: 671px; height: 683px;
    border-radius: 12px;
    background: linear-gradient(135deg, var(--panel-bg-a) 30%, var(--panel-bg-b));
    box-shadow: 0 6px 8px rgba(0,0,0,0.35);
  }
  .league-intro {
    position: absolute; left: 30px; top: 18px;
    font-size: 18px; font-weight: 400; color: var(--accent-red);
  }
  .league-table {
    position: absolute; left: 23px; top: 52px;
    border-collapse: separate; border-spacing: 7px 7.3px;
  }
  .league-table th {
    background: var(--headcell-bg); color: var(--headcell-text);
    background-clip: padding-box;
    border-bottom: 4px solid transparent;
    font-weight: 600; font-size: 16px; height: 37px; padding: 0;
    text-shadow: 0 1px 1px rgba(0,0,0,0.5);
  }
  .league-table td {
    background: var(--cell-bg); height: 32.3px; font-size: 17px; padding-top: 0; padding-bottom: 0;
    box-shadow: inset 0 2px 2px rgba(0,0,0,0.12);
    color: var(--text-dark); font-weight: 300;
  }
  .col-pos { width: 134px; text-align: center; }
  .col-name { width: 322px; }
  .col-pts { width: 134px; }
  td.col-pos { font-weight: 600; color: var(--text-strong); }
  td.col-name { padding-left: 63px; }
  td.col-pts { padding-left: 16px; }
  .mail-footer {
    position: absolute; left: 0; top: 917px; width: 1200px; height: 91px;
    background: var(--footer-bg);
    border-top: 1px solid #ddd;
    display: flex; align-items: center; justify-content: center;
    padding-bottom: 10px;
    font-size: 17px; font-weight: 400; color: #222;
  }
</style>
</head>
<body>
  <header class="mail-header">
    <div class="sender">
      <span class="sender-from">From</span>
      <span class="sender-brand">tolvex startline</span>
    </div>
  </header>

  <section class="league-panel">
    <p class="league-intro">See how you are doing! Are your friends doing better or worse?</p>
    <table class="league-table">
      <thead>
        <tr><th class="col-pos">POSITION</th><th class="col-name">NAME</th><th class="col-pts">POINTS</th></tr>
      </thead>
      <tbody>
        <tr><td class="col-pos">1</td><td class="col-name">Marcus Lindell</td><td class="col-pts">3519</td></tr>
        <tr><td class="col-pos">2</td><td class="col-name">Felix Harrow</td><td class="col-pts">2408</td></tr>
        <tr><td class="col-pos">3</td><td class="col-name">Daniel Pemberly</td><td class="col-pts">1956</td></tr>
        <tr><td class="col-pos">4</td><td class="col-name">Ruth Calloway</td><td class="col-pts">1813</td></tr>
        <tr><td class="col-pos">5</td><td class="col-name">Edgar Whitlow</td><td class="col-pts">486</td></tr>
        <tr><td class="col-pos">6</td><td class="col-name">Henrik Solberg</td><td class="col-pts">153</td></tr>
        <tr><td class="col-pos">7</td><td class="col-name">Sam Fenwick</td><td class="col-pts">-130</td></tr>
        <tr><td class="col-pos">8</td><td class="col-name">Ravi Tamworth</td><td class="col-pts">-323</td></tr>
        <tr><td class="col-pos">9</td><td class="col-name">Kola Adebisi</td><td class="col-pts">-577</td></tr>
        <tr><td class="col-pos">10</td><td class="col-name">Neil Ashcombe</td><td class="col-pts">-1672</td></tr>
        <tr><td class="col-pos">11</td><td class="col-name">Marcus Lindell</td><td class="col-pts">-1900</td></tr>
        <tr><td class="col-pos">12</td><td class="col-name">Felix Harrow</td><td class="col-pts">-2315</td></tr>
        <tr><td class="col-pos">13</td><td class="col-name">Daniel Pemberly</td><td class="col-pts">-2759</td></tr>
        <tr><td class="col-pos">14</td><td class="col-name">Ruth Calloway</td><td class="col-pts">-3001</td></tr>
      </tbody>
    </table>
  </section>

  <footer class="mail-footer">Don't forget to play NATIONS SHIELD QUAL 2 !</footer>
</body>
</html>
```